Supplement Bottle Packaging and Design

We want to rebrand our current health supplements (see below). We do want it to be modern, vibrant and appealing supplement bottles. Very upscale and elegant as it targets primarily women.
NOTE: READ THE ATTACHED WORD DOCUMENT!
Bottle size: We are totally open to the bottle size and shape, as long it's a typical supplement bottle size to handle 90-120 capsules; what we mostly need is new bottle design/packaging. YOU DON’T HAVE TO USE THE CURRENT WHITE BOTTLE SHAPE, BUT ANYTHING MORE MODERN WOULD WORK!
Updates
We need more modern, clean sleek designs to choose from
Look and feel
Each slider illustrates characteristics of the customer's brand and the style your logo design should communicate.

```html
<!DOCTYPE html>
<html lang="en">
<head>
<meta charset="UTF-8">
<title>Gentle Core – Oxygenating Colon Cleanse Label</title>
<link href="https://fonts.googleapis.com/css2?family=Montserrat:wght@400;600;700;800&display=swap" rel="stylesheet">
<style>
  :root {
    --page-bg: #ffffff;
    --label-red: #c4141a;
    --label-red-light: #e63a3c;
    --label-red-dark: #8e0c10;
    --band-red: #ee4446;
    --ring-red: #ff2a2e;
    --text-white: #ffffff;
    --text-soft: #f1eeee;
  }
  * { margin: 0; padding: 0; box-sizing: border-box; }
  html, body {
    width: 1200px;
    height: 1200px;
    overflow: hidden;
    background: var(--page-bg);
  }
  .canvas {
    position: relative;
    width: 1200px;
    height: 1200px;
    background: var(--page-bg);
  }
  .label {
    position: absolute;
    left: 220px;
    top: 100px;
    width: 760px;
    height: 1000px;
    overflow: hidden;
    background: linear-gradient(90deg,
      var(--label-red-light) 0%,
      var(--label-red) 14%,
      var(--label-red) 30%,
      var(--label-red-dark) 55%,
      var(--label-red) 80%,
      var(--label-red-light) 100%);
    font-family: 'Montserrat', sans-serif;
    color: var(--text-white);
  }
  .label__rings {
    position: absolute;
    left: -106px;
    top: 352px;
    width: 426px;
    height: 426px;
  }
  .label__stomach {
    position: absolute;
    left: 30px;
    top: 440px;
    width: 150px;
    height: 250px;
    border-radius: 70px 40px 90px 60px;
    background: radial-gradient(circle at 50% 50%, rgba(255, 60, 60, 0.35), rgba(255, 60, 60, 0.12));
  }
  .label__name {
    position: absolute;
    left: 0;
    right: 0;
    top: 58px;
    text-align: center;
    font-weight: 700;
    font-size: 164px;
    line-height: 176px;
    letter-spacing: -2px;
    color: var(--text-soft);
    text-shadow: 0 4px 14px rgba(0, 0, 0, 0.35);
  }
  .label__claim {
    position: absolute;
    left: 120px;
    right: 0;
    top: 462px;
    text-align: center;
    font-weight: 600;
    font-size: 66px;
    line-height: 70px;
    color: var(--text-soft);
    text-shadow: 0 3px 10px rgba(0, 0, 0, 0.3);
  }
  .label__type {
    position: absolute;
    left: 0;
    right: 0;
    top: 790px;
    text-align: center;
    font-weight: 400;
    font-size: 36px;
    letter-spacing: 9px;
    padding-left: 40px;
  }
  .label__band {
    position: absolute;
    left: 0;
    bottom: 0;
    width: 760px;
    height: 145px;
  }
  .label__count {
    position: absolute;
    left: 120px;
    right: 110px;
    top: 880px;
    text-align: center;
    font-weight: 700;
    font-size: 40px;
    line-height: 56px;
    letter-spacing: 1px;
  }
</style>
</head>
<body>
<main class="canvas">
  <section class="label">
    <svg class="label__rings" viewBox="0 0 426 426" aria-hidden="true">
      <circle cx="213" cy="213" r="206" fill="none" stroke="var(--ring-red)" stroke-width="6" opacity="0.55"/>
      <circle cx="213" cy="213" r="186" fill="none" stroke="var(--ring-red)" stroke-width="6" opacity="0.55"/>
    </svg>
    <div class="label__stomach" role="img" aria-label="Line icon of a stomach"></div>

    <h1 class="label__name">Gentle<br>Core</h1>
    <p class="label__claim">Oxygenating<br>Colon<br>Cleanse*</p>
    <p class="label__type">DIETARY SUPPLEMENT</p>

    <svg class="label__band" viewBox="0 0 760 145" aria-hidden="true">
      <path d="M0 70 H90 C115 70 110 0 150 0 H610 C650 0 645 70 670 70 H760 V145 H0 Z" fill="var(--band-red)"/>
    </svg>
    <p class="label__count">90 VEGETABLE<br>CAPSULES</p>
  </section>
</main>
</body>
</html>
```